Lorvena Aesthetic Doctor

I require an elegant, luxurious looking business card for my aesthetic business. I am a doctor and that will set me aside from competitors. I am planning to provide home and spa based treatments to clients with high expectations. I have attached my logo.

```html
<!DOCTYPE html>
<html lang="en">
<head>
<meta charset="utf-8">
<title>Lorvena Aesthetic Doctor – Business Card</title>
<link href="https://fonts.googleapis.com/css2?family=Lato:wght@300;400;700;900&display=swap" rel="stylesheet">
<style>
  :root {
    --bg: #e9ebef;
    --card: #ffffff;
    --ink: #1d1d22;
    --grey: #8a8d93;
    --grey-light: #c9cbd0;
    --blue: #2f7fd0;
    --blue-sky: #5aa9e6;
    --blue-deep: #2a55b8;
    --periwinkle: #7b8fe0;
  }
  * { box-sizing: border-box; margin: 0; padding: 0; }
  html, body { width: 1200px; height: 1200px; overflow: hidden; }
  body {
    background: var(--bg);
    font-family: "Lato", sans-serif;
    color: var(--ink);
    position: relative;
  }
  .card {
    position: absolute;
    left: 150px;
    width: 900px;
    height: 514px;
    background: var(--card);
    overflow: hidden;
    box-shadow: 0 6px 22px rgba(0,0,0,0.12);
  }
  .card--front { top: 50px; }
  .card--back { top: 630px; }

  .card__art { position: absolute; inset: 0; width: 100%; height: 100%; }

  /* Brand lockup */
  .brand {
    position: absolute;
    display: flex;
    align-items: center;
    gap: 12px;
  }
  .brand__mark {
    width: 52px; height: 52px;
    border: 3px solid var(--grey-light);
    border-radius: 50%;
    flex: none;
  }
  .brand__name {
    font-weight: 400;
    color: var(--grey);
    font-size: 22px;
    line-height: 1.15;
    letter-spacing: 1.5px;
    text-transform: uppercase;
    white-space: nowrap;
  }
  .card--front .brand { left: 36px; top: 225px; }
  .card--back .brand { right: 40px; top: 190px; }
  .card--back .brand__mark { width: 58px; height: 58px; }
  .card--back .brand__name { font-size: 28px; letter-spacing: 3px; }

  /* Front headline */
  .headline {
    position: absolute;
    left: 500px;
    top: 170px;
    color: #fff;
    font-size: 44px;
    font-weight: 400;
    line-height: 1.1;
    text-transform: uppercase;
    letter-spacing: 0.5px;
  }
  .headline strong { font-weight: 900; }

  /* Back details */
  .person { position: absolute; left: 60px; top: 48px; width: 520px; }
  .person__name { font-size: 30px; font-weight: 700; }
  .person__creds { font-size: 16px; font-weight: 400; color: var(--blue); margin-left: 6px; letter-spacing: 0.5px; }
  .person__diploma { font-size: 15px; font-style: italic; color: var(--grey); font-weight: 300; margin-top: 2px; }
  .divider {
    position: absolute; left: 60px; top: 118px; width: 800px; height: 1px;
    background: var(--grey-light);
  }
  .contact { position: absolute; left: 60px; top: 140px; list-style: none; }
  .contact__item {
    display: flex; align-items: center; gap: 10px;
    font-size: 20px; line-height: 32px;
  }
  .contact__icon { width: 18px; height: 18px; fill: none; stroke: var(--blue-deep); stroke-width: 2; }

  .services {
    position: absolute; left: 60px; top: 275px;
    font-size: 22px; line-height: 32px; text-transform: uppercase; letter-spacing: 0.5px;
  }
  .services__row { display: flex; align-items: center; gap: 12px; }
  .services__dot { width: 11px; height: 11px; border-radius: 50%; background: var(--blue-sky); }
  .tagline {
    position: absolute; left: 60px; top: 350px;
    font-size: 22px; font-weight: 900; letter-spacing: 6px; text-transform: uppercase;
  }
</style>
</head>
<body>

<section class="card card--front">
  <svg class="card__art" viewBox="0 0 900 514" role="img" aria-label="Painterly brushed texture in shades of blue filling the right side of the card">
    <defs>
      <linearGradient id="paint" x1="0" y1="0" x2="1" y2="1">
        <stop offset="0" stop-color="#3f7fd8"/>
        <stop offset="0.45" stop-color="#5aa3e6"/>
        <stop offset="0.75" stop-color="#2f63c4"/>
        <stop offset="1" stop-color="#6fb6ea"/>
      </linearGradient>
    </defs>
    <path d="M250 0 C 360 110, 470 200, 420 514 L900 514 L900 0 Z" fill="#b9bcc3"/>
    <path d="M268 0 C 380 110, 488 200, 440 514 L900 514 L900 0 Z" fill="#7b8fe0"/>
    <path d="M285 0 C 398 110, 505 200, 458 514 L900 514 L900 0 Z" fill="url(#paint)"/>
  </svg>
  <div class="brand">
    <span class="brand__mark"></span>
    <span class="brand__name">Lorvena<br>Aesthetic Doctor</span>
  </div>
  <h1 class="headline"><strong>Home</strong> and <strong>Spa</strong><br>Based <strong>Treatments</strong></h1>
</section>

<section class="card card--back">
  <svg class="card__art" viewBox="0 0 900 514" role="img" aria-label="Strip of painterly blue texture along the lower right edge">
    <defs>
      <linearGradient id="paint2" x1="0" y1="0" x2="1" y2="0">
        <stop offset="0" stop-color="#5aa3e6"/>
        <stop offset="0.6" stop-color="#3f7fd8"/>
        <stop offset="1" stop-color="#7cbcec"/>
      </linearGradient>
    </defs>
    <polygon points="520,514 900,400 900,514" fill="url(#paint2)"/>
  </svg>

  <div class="person">
    <p class="person__name">Dr Mirela Kost<span class="person__creds">MRCPCH MD</span></p>
    <p class="person__diploma">Australasian Diploma of Aesthetic Medicine</p>
  </div>
  <div class="divider"></div>

  <ul class="contact">
    <li class="contact__item">
      <svg class="contact__icon" viewBox="0 0 24 24"><path d="M5 3h4l2 5-3 2a12 12 0 0 0 6 6l2-3 5 2v4a2 2 0 0 1-2 2A18 18 0 0 1 3 5a2 2 0 0 1 2-2z"/></svg>
      0800 555 019
    </li>
    <li class="contact__item">
      <svg class="contact__icon" viewBox="0 0 24 24"><rect x="3" y="5" width="18" height="14"/><path d="M3 5l9 8 9-8"/></svg>
      mirela@lorvena.co.nz
    </li>
    <li class="contact__item">
      <svg class="contact__icon" viewBox="0 0 24 24"><circle cx="12" cy="12" r="9"/><path d="M3 12h18M12 3c3 3 3 15 0 18M12 3c-3 3-3 15 0 18"/></svg>
      www.lorvena.co.nz
    </li>
  </ul>

  <div class="brand">
    <span class="brand__mark"></span>
    <span class="brand__name">Lorvena<br>Aesthetic Doctor</span>
  </div>

  <div class="services">
    <p class="services__row">Dermal Injectables <span class="services__dot"></span> Plasma Facials <span class="services__dot"></span> Microneedling</p>
    <p class="services__row">Skin Boosters <span class="services__dot"></span> Excessive Sweating</p>
  </div>
  <p class="tagline">Home and Spa Based Treatments</p>
</section>

</body>
</html>
```